Velmar Ops Business Cards

We need to design some upbeat business cards. We are an Industrial Rope Access Company/Height Safety Company that specialize in Rope Access, Confined Space, Anchor Points, Safety Systems, PPE Inspecions and Rigging.
Company name is Velmar Ops Ltd
Card is for Gareth Lomas the Company Director
His mobile number is 027 418 9072 and email is gareth@velmarops.co.nz. Website address is www.velmarops.co.nz.
We will post some pictures below to ensure you get a good idea of what we do.

```html
<!DOCTYPE html>
<html lang="en">
<head>
<meta charset="utf-8">
<title>Velmar Ops Ltd – Business Cards</title>
<link rel="stylesheet" href="https://fonts.googleapis.com/css2?family=Noto+Serif:wdth,wght@62.5..100,400..700&family=Oswald:wght@400&family=Roboto+Condensed:wght@400&display=swap">
<style>
  :root {
    --backdrop: #777674;
    --navy: #1a1a52;
    --navy-mid: #2a2b60;
    --navy-light: #35376b;
    --cream: #ebe7dc;
  }
  html, body {
    margin: 0;
    padding: 0;
    width: 1200px;
    height: 1200px;
    overflow: hidden;
    background: var(--backdrop);
  }
  .sheet {
    position: relative;
    width: 1200px;
    height: 1200px;
  }
  .card {
    position: absolute;
    left: 180px;
    width: 840px;
    height: 480px;
    overflow: hidden;
  }

  /* Front */
  .card-front {
    top: 78px;
    background: linear-gradient(180deg, var(--navy) 0%, var(--navy) 22%, var(--navy-mid) 50%, var(--navy) 72%, var(--navy) 100%);
  }
  .brand-stripe {
    position: absolute;
    left: 110px;
    top: 0;
    width: 124px;
    height: 480px;
    background: var(--cream);
  }
  .brand-stripe-name {
    position: absolute;
    left: 62px;
    top: 240px;
    transform: translate(-50%, -50%) rotate(-90deg);
    white-space: nowrap;
    margin: 0;
    font-family: "Noto Serif", serif;
    font-weight: 700;
    font-stretch: 87%;
    font-size: 50px;
    line-height: 1;
    letter-spacing: 1px;
    color: var(--navy);
  }
  .person {
    position: absolute;
    left: 420px;
    top: 170px;
    color: var(--cream);
  }
  .person-name {
    margin: 0;
    font-family: "Oswald", sans-serif;
    font-weight: 400;
    font-size: 76px;
    line-height: 1;
    letter-spacing: 1px;
  }
  .person-role {
    margin: 6px 0 0;
    font-family: "Roboto Condensed", sans-serif;
    font-weight: 400;
    font-size: 37px;
    line-height: 1.1;
  }

  /* Back */
  .card-back {
    top: 600px;
    background: var(--navy-mid);
  }
  .back-backdrop {
    position: absolute;
    inset: 0;
    background: radial-gradient(ellipse at 50% 55%, var(--navy-light) 0%, var(--navy-mid) 55%, #23245a 100%);
  }
  .company-name {
    position: absolute;
    left: 0;
    right: 0;
    top: 180px;
    margin: 0;
    text-align: center;
    font-family: "Noto Serif", serif;
    font-weight: 700;
    font-stretch: 70%;
    font-size: 62px;
    line-height: 1;
    color: var(--cream);
  }
  .contact-list {
    position: absolute;
    left: 420px;
    top: 296px;
    margin: 0;
    padding: 0;
    list-style: none;
  }
  .contact-item {
    display: flex;
    align-items: center;
    height: 36px;
    margin-bottom: 2px;
    font-family: "Noto Serif", serif;
    font-weight: 700;
    font-size: 21px;
    color: var(--cream);
  }
  .contact-item:last-child { margin-top: 4px; }
  .contact-icon {
    width: 36px;
    height: 24px;
    margin-right: 16px;
    fill: var(--cream);
    stroke: var(--cream);
  }
</style>
</head>
<body>
<main class="sheet">

  <section class="card card-front" aria-label="Card front">
    <div class="brand-stripe">
      <p class="brand-stripe-name">VELMAR OPS LTD</p>
    </div>
    <div class="person">
      <h1 class="person-name">GARETH LOMAS</h1>
      <p class="person-role">Company Director</p>
    </div>
  </section>

  <section class="card card-back" aria-label="Card back">
    <div class="back-backdrop" role="img" aria-label="Faint photograph of a large suspension bridge with rope access work, in navy tones"></div>
    <h2 class="company-name">VELMAR OPS LTD</h2>
    <ul class="contact-list">
      <li class="contact-item">
        <svg class="contact-icon" viewBox="0 0 36 24" aria-hidden="true">
          <path stroke="none" d="M2 8 C2 2 34 2 34 8 L34 10 L26 10 L26 7 L10 7 L10 10 L2 10 Z"/>
          <path stroke="none" d="M8 11 L28 11 L33 23 L3 23 Z"/>
          <circle cx="18" cy="17" r="3.5" fill="#2a2b60" stroke="none"/>
        </svg>
        027 418 9072
      </li>
      <li class="contact-item">
        <svg class="contact-icon" viewBox="0 0 36 24" aria-hidden="true">
          <rect x="2" y="4" width="32" height="16" fill="none" stroke-width="2"/>
          <path d="M2 4 L18 14 L34 4 M2 20 L14 11 M34 20 L22 11" fill="none" stroke-width="2"/>
        </svg>
        gareth@velmarops.co.nz
      </li>
      <li class="contact-item">
        <svg class="contact-icon" viewBox="0 0 36 24" aria-hidden="true">
          <g fill="none" stroke-width="1.6">
            <circle cx="22" cy="12" r="10"/>
            <ellipse cx="22" cy="12" rx="4.5" ry="10"/>
            <line x1="12" y1="12" x2="32" y2="12"/>
            <path d="M14 7 H30 M14 17 H30"/>
          </g>
        </svg>
        www.velmarops.nz.com
      </li>
    </ul>
  </section>

</main>
</body>
</html>
```